An innovative software company needs a business card!

We need a business card design for our new innovative software company. Please use the details for the business card provided in business card details section. We will use the business card paper like: https://www.prindlecard.example/us/products/nfc/business-cards-plus.html Our company name: celvane We have already a logo and colors to use in business cards too ,

Target Market(s)

App & Sofware Development

Industry/Entity Type

Software

Contact Information for Business Card

Lukas Brenner, BSc.
Owner and Creative Superhero

Adress:
Pelzerweg 14/3/1708
A - 1100, Wien

Tel: +43 (0) 664 219 53 08
Email: lukas.brenner@celvane.example
Web: www.celvane.example

Requirements
Must have
• - Use our logo
Nice to have
• It would be nice to have a nice picture on the backside. (About apps, software, technicals or funy stuff) - Use our colors as in business card (optional)

```html
<!DOCTYPE html>
<html lang="en">
<head>
<meta charset="utf-8">
<title>celvane – Business Card</title>
<link rel="stylesheet" href="https://fonts.googleapis.com/css2?family=Montserrat:wght@400;500;700&display=swap">
<style>
  :root {
    --stage: #34444c;
    --card-black: #050607;
    --brand-blue: #27a3d1;
    --panel-blue: #2298c6;
    --name-grey: #c9cdd0;
    --mark-grey: #c4c6c8;
    --ink-white: #ffffff;
  }
  html, body {
    margin: 0;
    padding: 0;
    width: 1200px;
    height: 900px;
    overflow: hidden;
    background: var(--stage);
    font-family: "Montserrat", sans-serif;
  }
  .canvas {
    position: relative;
    width: 1200px;
    height: 900px;
    display: flex;
    flex-direction: column;
    align-items: center;
    justify-content: center;
    gap: 40px;
  }
  .card {
    width: 700px;
    height: 390px;
    display: block;
    box-shadow: 0 10px 28px rgba(0, 0, 0, 0.35);
  }
  .card-bg { fill: var(--card-black); }
  .contact-panel { fill: var(--panel-blue); }
  .holder-name {
    font-family: "Montserrat", sans-serif;
    font-weight: 500;
    font-size: 34px;
    fill: var(--name-grey);
  }
  .holder-title {
    font-family: "Montserrat", sans-serif;
    font-weight: 400;
    font-size: 19px;
    fill: var(--name-grey);
  }
  .contact-line {
    font-family: "Montserrat", sans-serif;
    font-weight: 500;
    font-size: 16px;
    fill: var(--ink-white);
  }
  .contact-line.small { font-size: 13.5px; }
  .contact-icon {
    fill: none;
    stroke: var(--ink-white);
    stroke-width: 1.8;
    stroke-linecap: round;
    stroke-linejoin: round;
  }
  .brand-name {
    font-family: "Montserrat", sans-serif;
    font-weight: 700;
    fill: var(--brand-blue);
  }
  .brand-dot { fill: var(--mark-grey); }
</style>
</head>
<body>
<main class="canvas">

  <!-- Front side -->
  <svg class="card card-front" viewBox="0 0 700 390" xmlns="http://www.w3.org/2000/svg" aria-label="Business card front">
    <rect class="card-bg" width="700" height="390"/>
    <polygon class="contact-panel" points="0,0 700,0 0,300"/>

    <text class="holder-name" x="36" y="56">Lukas Brenner, BSc.</text>
    <text class="holder-title" x="36" y="84">Owner and Creative Superhero</text>

    <!-- web -->
    <g class="contact-icon" transform="translate(38,108)">
      <circle cx="10" cy="10" r="9"/>
      <ellipse cx="10" cy="10" rx="4" ry="9"/>
      <line x1="1" y1="10" x2="19" y2="10"/>
    </g>
    <text class="contact-line" x="70" y="124">www.celvane.example</text>

    <!-- email -->
    <g class="contact-icon" transform="translate(36,140)">
      <rect x="1" y="2" width="22" height="15" rx="1"/>
      <polyline points="1,3 12,11 23,3"/>
    </g>
    <text class="contact-line" x="70" y="155">lukas.brenner@celvane.example</text>

    <!-- phone -->
    <g class="contact-icon" transform="translate(37,170)">
      <path d="M4 2 L8 2 L10 7 L7 9 C8.5 12.5 11 15 14 16.5 L16 13.5 L21 15.5 L21 19.5 C12 20 3 11 4 2 Z"/>
    </g>
    <text class="contact-line" x="70" y="187">+43 (0) 664 219 53 08</text>

    <!-- address -->
    <g class="contact-icon" transform="translate(38,202)">
      <path d="M10 22 C4 14 3 11 3 8 A7 7 0 0 1 17 8 C17 11 16 14 10 22 Z"/>
      <circle cx="10" cy="8" r="2.5"/>
    </g>
    <text class="contact-line small" x="70" y="214">Pelzerweg 14/3/1708</text>
    <text class="contact-line small" x="82" y="231">A - 1100, Wien</text>

    <circle class="brand-dot" cx="600" cy="190" r="38"/>
    <text class="brand-name" x="668" y="335" font-size="66" text-anchor="end">celvane</text>
  </svg>

  <!-- Back side -->
  <svg class="card card-back" viewBox="0 0 700 390" xmlns="http://www.w3.org/2000/svg" aria-label="Business card back">
    <rect class="card-bg" width="700" height="390"/>
    <circle class="brand-dot" cx="150" cy="195" r="58"/>
    <text class="brand-name" x="236" y="224" font-size="82">celvane</text>
  </svg>

</main>
</body>
</html>
```